Disposable food packaging business needs a product box design

We are looking for the design layout for our coffee cup cartons. They will be printed on white boxes and we would like them to be recognizable from a distance. These will not be seen by the customers buying coffee and the design is primarily for the Warehouse staff.
see attached a basic mockup and the type of cups that will be inside the cartons, creative freedom is still welcome, we are trying to achieve a more professional look.
Box size will be approximately 46cm wide, 50cm high and 38cm depth.
Things we would like.
- We would like our brand name 'RVT' to be one of the first things you notice. looking for a design for the brand/ logo.
-Each cup comes in multiple colours (black, white, rainbow, kraft (brown), we would like each box to have the colour of the cup incorporated into the design as well as the colour in writing. So that the colour of the cups is obvious.
-Each cup comes in multiple sizes (4oz, 6oz, 8oz, 8oz squat, 12oz and 16oz) that will need to be easily seen.
-A re-order code (example; HCP610).
-Carton quantity 1000 and inner sleeve qty 50.
-A barcode.
-Include attached symbols (eco friendly symbol to be black to match the rest).
So eventually there will be a total of 24 different coffee cup boxes- each with the same basic info.
-RVT brand
-Cup Colour (White, black, kraft and rainbow)
-Cup size (4, 6, 8, 8 squat, 12 and 16)
-Cup code (HCPxxx- xxx will be different for each cup/size)
-Carton qty 1000 sleeve qty 50 (same for every size and colour.
-Barcode (supplied later)
Initially just provide the generic design/ layout of one box- the successful designer will need to produce the design for all combinations.
NOTE - we are looking for the design of the outer carton for coffee cups. These cartons are for delivery of cups to cafes etc. They are not seen by the customer who purchases a coffee. The main requirement is for the warehouse staff to be able to easily identify and select the correct style and colour of cups.
Each carton contains 1000 cups.

```html
<!DOCTYPE html>
<html lang="en">
<head>
<meta charset="utf-8">
<title>RVT Coffee Cups Carton – 12oz White</title>
<link rel="stylesheet" href="https://fonts.googleapis.com/css2?family=Montserrat:wght@500;600;800&display=swap">
<style>
  :root {
    --backdrop: #a4a6a9;
    --board: #f3f2ef;
    --ink: #3a322e;
    --band: #1b1515;
    --ghost: #cbc9c6;
    --crease: #dcdad6;
  }
  * { margin: 0; padding: 0; box-sizing: border-box; }
  html, body { width: 1200px; height: 685px; overflow: hidden; }
  body {
    background: var(--backdrop);
    font-family: "Montserrat", sans-serif;
    color: var(--ink);
    position: relative;
  }
  .carton {
    position: absolute;
    left: 213px;
    top: 112px;
    width: 773px;
    height: 460px;
    display: flex;
  }
  .panel {
    position: relative;
    height: 100%;
    background: var(--board);
    overflow: hidden;
  }
  .panel--side { width: 350px; border-right: 1px solid var(--crease); }
  .panel--front { width: 423px; }
  .band { position: absolute; inset: 0; width: 100%; height: 100%; }
  .size-colour {
    position: absolute;
    font-weight: 500;
    font-size: 40px;
    white-space: nowrap;
    transform-origin: left bottom;
    letter-spacing: -0.5px;
  }
  .size-colour .divider {
    display: inline-block;
    width: 2px;
    height: 44px;
    background: var(--ink);
    margin: 0 12px;
    vertical-align: -8px;
  }
  .panel--side .size-colour { left: 16px; top: 278px; transform: rotate(3deg); font-size: 34px; }
  .panel--front .size-colour { left: 22px; top: 262px; transform: rotate(-15.2deg); }
  .brand-strip {
    position: absolute;
    left: 248px;
    top: 0;
    width: 100px;
    height: 100%;
    display: flex;
    align-items: center;
    justify-content: center;
  }
  .brand-strip span {
    transform: rotate(90deg);
    font-weight: 800;
    font-size: 150px;
    color: var(--ghost);
    letter-spacing: 4px;
    white-space: nowrap;
  }
  .product-block {
    position: absolute;
    right: 38px;
    top: 262px;
    text-align: right;
  }
  .brand-name { font-weight: 800; font-size: 58px; line-height: 0.9; letter-spacing: -1px; }
  .product-name { font-weight: 800; font-size: 19px; line-height: 1.1; }
  .reorder-code {
    display: inline-block;
    margin-top: 3px;
    border: 2px solid var(--ink);
    font-weight: 800;
    font-size: 15px;
    padding: 0 5px;
    line-height: 1.25;
  }
  .quantity { font-size: 9px; font-weight: 600; margin-top: 2px; }
  .badges {
    position: absolute;
    right: 38px;
    top: 395px;
    display: flex;
    align-items: center;
    gap: 12px;
  }
  .badge { width: 40px; height: 40px; }
  .badge-sep { width: 3px; height: 3px; background: var(--ink); border-radius: 50%; }
</style>
</head>
<body>
  <main class="carton">
    <section class="panel panel--side">
      <div class="brand-strip"><span>RVT</span></div>
      <svg class="band" viewBox="0 0 350 460" preserveAspectRatio="none" aria-hidden="true">
        <polygon points="0,342 350,322 350,338 0,358" fill="var(--band)"/>
      </svg>
      <p class="size-colour">12oz<span class="divider"></span>White</p>
    </section>

    <section class="panel panel--front">
      <svg class="band" viewBox="0 0 423 460" preserveAspectRatio="none" aria-hidden="true">
        <polygon points="0,322 423,206 423,222 0,338" fill="var(--band)"/>
      </svg>
      <p class="size-colour">12oz<span class="divider"></span>White</p>

      <div class="product-block">
        <p class="brand-name">RVT</p>
        <p class="product-name">COFFEE CUPS</p>
        <p class="reorder-code">RCP314</p>
        <p class="quantity">Qty - 1000 (50X20)</p>
      </div>

      <div class="badges">
        <svg class="badge" viewBox="0 0 40 40" aria-label="Aqueous coating">
          <circle cx="20" cy="20" r="17" fill="none" stroke="var(--ink)" stroke-width="1.6"/>
          <path d="M20 10 C16 17 14 20 14 23 a6 6 0 0 0 12 0 c0-3-2-6-6-13z" fill="var(--ink)"/>
        </svg>
        <span class="badge-sep"></span>
        <svg class="badge" viewBox="0 0 40 40" aria-label="Home compostable badge">
          <circle cx="20" cy="20" r="17" fill="none" stroke="var(--ink)" stroke-width="1.6"/>
        </svg>
        <span class="badge-sep"></span>
        <svg class="badge" viewBox="0 0 40 40" aria-label="Eco friendly badge">
          <circle cx="20" cy="20" r="17" fill="none" stroke="var(--ink)" stroke-width="1.6"/>
        </svg>
      </div>
    </section>
  </main>
</body>
</html>
```